Tiroler party ecommerce site

We have a eCommerce site that needs a redesign. What we need are 3 pages: a frontpage, a product listing page and a product page.

The look has to be:
fun, modern, fresh, bright, professional look but not corporate.

Some content keywords are :
Carnival, oktoberfesten, tirol, dirndl, leder hosen, beer, women with big breast (no porn! just fun)

Some functional hints :

The frontpage needs to give a good impression of all the products on the site.
There should also be some space for campaigns or banners on the frontpage.

The product listing page should have facets (search options) and a search field.

The product page should have a few boxes such as related products, others viewed, comments etc.. (your average product page content)

All pages should show a small cart button or box and off course a kick ass menu!

Some links :

The current site http://www.feestkraamwinkel.nl/

We couldn't find any site to show as inspiration most party sites are very bad!.

```html
<!DOCTYPE html>
<html lang="nl">
<head>
<meta charset="utf-8">
<title>Feestkraamwinkel – Tyrolean and apres ski articles</title>
<link href="https://fonts.googleapis.com/css2?family=Oswald:wght@400;500;700&display=swap" rel="stylesheet">
<style>
:root{
  --green:#0b6b12;
  --green-dark:#075a0d;
  --gold:#a8862f;
  --cream:#f1eadb;
  --frame:#d8c7a5;
  --ink:#333;
  --muted:#555;
  --header:#2b2b2b;
}
*{box-sizing:border-box;margin:0;padding:0}
html,body{width:937px;height:1200px;overflow:hidden}
body{position:relative;font-family:Arial,Helvetica,sans-serif;color:var(--ink);
  background:#141414}
.forest{position:absolute;inset:0;
  background:radial-gradient(ellipse at 50% 30%,#8a6426 0%,#3b2a12 45%,#111 80%)}
.page{position:absolute;left:141px;top:0;width:655px;height:1130px;background:var(--cream)}
.abs{position:absolute}
.topbar{left:0;top:0;width:655px;height:26px;background:var(--green)}
.search{left:6px;top:5px;width:138px;height:17px;background:var(--green-dark);color:#cfe3cf;font-size:7px;padding:4px 8px}
.search svg{position:absolute;right:8px;top:3px}
.account{right:18px;top:9px;font-size:7px;color:#fff;letter-spacing:.2px}
.account span{margin-left:16px}
.header{left:0;top:26px;width:655px;height:50px;background:linear-gradient(#3a3a3a,#1e1e1e)}
.brand{left:13px;top:10px;font-family:Oswald,sans-serif;font-size:24px;color:#fff;font-weight:400}
.nav{right:0;top:0;height:50px;display:flex}
.nav a{display:block;height:50px;line-height:50px;padding:0 19px;color:#fff;font-family:Oswald,sans-serif;font-size:9px;border-left:1px solid #111;text-decoration:none}
.nav a.active{background:linear-gradient(#555,#333)}
.hero{left:0;top:76px;width:655px;height:282px;background:linear-gradient(90deg,#b97a22,#e9b456 45%,#f6d58f 75%,#f3d28a)}
.hero-photo{left:110px;top:10px;width:260px;height:272px;background:linear-gradient(#2a1a08,#120b03);border-radius:40% 40% 0 0}
.hero h1{left:366px;top:66px;font-family:Oswald,sans-serif;font-weight:700;font-size:31px;color:var(--green)}
.hero h2{left:369px;top:103px;font-family:Oswald,sans-serif;font-weight:400;font-size:16px;color:#111}
.hero p{left:372px;top:130px;width:250px;font-family:Oswald,sans-serif;font-size:7px;line-height:14px;color:#222}
.buy{left:372px;top:182px;width:107px;height:31px;background:var(--green);color:#fff;font-family:Oswald,sans-serif;font-weight:500;font-size:14px;text-align:center;line-height:31px}
.slide-arrows{right:12px;top:259px;display:flex;gap:2px}
.slide-arrows div{width:12px;height:12px;background:#b58a3a;color:#fff;font-size:9px;text-align:center;line-height:12px}
.catnav{left:0;top:358px;width:655px;height:28px;background:var(--green);display:flex;justify-content:space-around;align-items:center}
.catnav span{font-family:Oswald,sans-serif;font-size:9px;color:#fff}
.intro{left:21px;top:404px;width:620px;font-size:7.5px;font-style:italic;line-height:15px;color:var(--muted)}
.products{left:30px;top:453px;width:595px;display:flex;justify-content:space-between}
.product{width:136px;text-align:center}
.frame{width:136px;height:126px;border:5px solid var(--frame);background:#fff}
.frame div{width:100%;height:100%;background:linear-gradient(#f4f1ec,#e4dccd)}
.product h3{margin-top:15px;font-family:Oswald,sans-serif;font-weight:400;font-size:10px;color:var(--green)}
.product .price{margin-top:8px;font-family:Oswald,sans-serif;font-size:13px;color:var(--gold)}
.chev{top:500px;font-size:24px;color:#b9a98b;font-weight:100}
.divider{left:15px;top:650px;width:623px;height:1px;background:#d9c9a8}
.sec-title{font-family:Oswald,sans-serif;font-weight:500;font-size:15px;color:var(--green)}
.about{left:19px;top:681px;width:222px}
.about p{font-size:7.5px;line-height:14.6px;color:var(--muted);margin-top:11px}
.about p:first-of-type{margin-top:13px}
.info{left:273px;top:681px;width:363px}
.info-arrows{right:0;top:0;display:flex;gap:1px}
.info-arrows div{width:13px;height:12px;background:#b8b2a6;color:#fff;font-size:9px;line-height:12px;text-align:center}
.card{top:29px;width:170px}
.card h4{font-family:Oswald,sans-serif;font-weight:500;font-size:11px;color:#333}
.card .pic{margin-top:6px;height:89px}
.card p{margin-top:11px;font-size:7.5px;line-height:14.6px;color:var(--muted)}
.more{margin-top:8px;width:63px;height:17px;background:var(--green);color:#fff;font-size:6.5px;text-align:center;line-height:17px}
.partners{left:16px;top:947px;width:623px;display:flex;justify-content:space-between}
.partner{width:141px;height:79px;border:5px solid var(--frame);background:#fff;display:flex;align-items:center;justify-content:center;font-family:Oswald,sans-serif;font-weight:500;font-size:16px;color:var(--green)}
.footer{left:15px;top:1047px;width:626px;height:70px;background:var(--green);color:#fff;font-size:7.5px}
.flinks{left:22px;top:20px}
.flinks span{margin-right:14px}
.copy{left:22px;top:41px}
.social{left:258px;top:25px;display:flex;gap:7px}
.social div{width:21px;height:21px;border-radius:50%;background:#fff}
.contact{left:436px;top:20px;line-height:18px}
.contact svg{vertical-align:-1px;margin-right:3px}
</style>
</head>
<body>
<div class="forest" role="img" aria-label="Dark forest with tree trunks at sunset"></div>
<main class="page">
  <div class="abs topbar">
    <div class="abs search">SEARCH :
      <svg width="10" height="10" viewBox="0 0 10 10"><circle cx="4" cy="4" r="3" fill="none" stroke="#9fbf9f" stroke-width="1.3"/><line x1="6.2" y1="6.2" x2="9" y2="9" stroke="#9fbf9f" stroke-width="1.5"/></svg>
    </div>
    <div class="abs account">YOUR CART IS : 0 ITEMS,<span>LOGIN</span><span>|</span><span>REGISTER</span></div>
  </div>
  <header class="abs header">
    <div class="abs brand">Feestkraamwinkel</div>
    <nav class="abs nav">
      <a class="active" href="#">HOME</a><a href="#">INFORMATION</a><a href="#">LEFT</a><a href="#">CONTACT</a>
    </nav>
  </header>
  <section class="abs hero">
    <div class="abs hero-photo" role="img" aria-label="Silhouette of a cowboy holding a lasso against a golden sky"></div>
    <h1 class="abs">FEESTKRAAM WINKEL</h1>
    <h2 class="abs">TYROLEAN AND APRES SKI ARTICLES</h2>
    <p class="abs">LOREM IPSUM IS SIMPLY DUMMY TEXT OF THE PRINTING AND TYPE-SETTING INDUSTRY. LOREM IPSUM HAS BEEN THE INDUSTRY'S STANDARD DUMMY TEXT EVER SINCE THE 1500S</p>
    <div class="abs buy">BUY NOW</div>
    <div class="abs slide-arrows"><div>‹</div><div>›</div></div>
  </section>
  <nav class="abs catnav">
    <span>TYROLEAN CLOTHING ▾</span><span>CLOTHING ACCESSORIES ▾</span><span>TIROLER SUSPEND ▾</span><span>TYROLEAN HATS ▾</span><span>DECORATIONS</span><span>GIFT ITEMS ▾</span>
  </nav>
  <p class="abs intro">Feestkraamwinkel.nl is de eerste webshop gespecialiseerd in Tiroler artikelen. Dus wanneer u een Tirools feestje heeft, of gewoon op zoek bent naar Tiroolse carnavalskleding, u bent bij ons gegarandeerd aan het juiste adres. Natuurlijk hebben wij ook alles voor een geweldig apres ski feest in ons assortiment.</p>
  <div class="abs chev" style="left:10px">‹</div>
  <div class="abs chev" style="right:10px">›</div>
  <section class="abs products">
    <div class="product"><div class="frame"><div role="img" aria-label="Blonde braided costume wig"></div></div><h3>LEDERHOSEN LONG</h3><div class="price">€ 12.90</div></div>
    <div class="product"><div class="frame"><div role="img" aria-label="Yellow and blue dirndl costume"></div></div><h3>LEDERHOSEN LONG</h3><div class="price">€ 12.90</div></div>
    <div class="product"><div class="frame"><div role="img" aria-label="Lederhosen outfit with checked shirt and hat"></div></div><h3>LEDERHOSEN LONG</h3><div class="price">€ 12.90</div></div>
    <div class="product"><div class="frame"><div role="img" aria-label="Apron printed with lederhosen"></div></div><h3>LEDERHOSEN LONG</h3><div class="price">€ 12.90</div></div>
  </section>
  <div class="abs divider"></div>
  <section class="abs about">
    <h2 class="sec-title">TYROLEAN AND APRES SKI ARTICLES</h2>
    <p>Willkommen in Tirol, of welkom in onze Tirool shop!</p>
    <p>Feestkraamwinkel.nl is de eerste webshop gespecialiseerd in Tiroler artikelen. Dus wanneer u een Tirools feestje heeft, of gewoon op zoek bent naar Tiroolse carnavalskleding, u bent bij ons gegarandeerd aan het juiste adres. Natuurlijk hebben wij ook alles voor een geweldig apres ski feest in ons assortiment.</p>
    <p>Wij bieden een zeer groot assortiment Tiroolse artikelen, waaronder kleding (zowel tiroler broeken als tiroolse jurkjes), hoeden, decoraties, bierpullen en spellen om jouw thema feest tot een succes te maken!</p>
    <p>Nieuw in ons assortiment zijn de Tiroler sexy shorten, ga met</p>
  </section>
  <section class="abs info">
    <h2 class="sec-title">INFORMATION</h2>
    <div class="abs info-arrows"><div>‹</div><div>›</div></div>
    <article class="abs card" style="left:0">
      <h4>SHIPPING</h4>
      <div class="pic" role="img" aria-label="Person wearing a brown leather apron" style="background:linear-gradient(90deg,#8d8a86,#5e4a3a 50%,#c9cdd0)"></div>
      <p>Feestkraamwinkel.nl is de eerste webshop gespecialiseerd in Tiroler artikelen. Dus wanneer u een Tirools feestje heeft, of gewoon op zoek bent naar Tiroolse carnavalskleding</p>
      <div class="more">READ MORE</div>
    </article>
    <article class="abs card" style="left:193px">
      <h4>STOCK</h4>
      <div class="pic" role="img" aria-label="Two children in cowboy hats" style="background:linear-gradient(90deg,#c89a5c,#8a5a2e 55%,#d9b27a)"></div>
      <p>Feestkraamwinkel.nl is de eerste webshop gespecialiseerd in Tiroler artikelen. Dus wanneer u een Tirools feestje heeft, of gewoon op zoek bent naar Tiroolse carnavalskleding</p>
      <div class="more">READ MORE</div>
    </article>
  </section>
  <section class="abs partners">
    <div class="partner">Partyhal</div>
    <div class="partner">Snelpost</div>
    <div class="partner">Betaalnu</div>
    <div class="partner">VeiligPay</div>
  </section>
  <footer class="abs footer">
    <div class="abs flinks"><span>Home</span><span>|</span><span>Information</span><span>|</span><span>Left</span><span>|</span><span>Contact</span></div>
    <div class="abs copy">Copyrights © 2014. Feestkraam Winkel. All Rights Reserved.</div>
    <div class="abs social"><div></div><div></div></div>
    <div class="abs contact">Marktstraat 12, 1234 AB DORPSVELDE<br>
      <svg width="8" height="8" viewBox="0 0 8 8"><path d="M1.5 0.5l1.5 0 .6 1.8-1 .8a4 4 0 0 0 2.3 2.3l.8-1 1.8.6 0 1.5c-3.5 .3-6.3-2.5-6-6z" fill="#fff"/></svg>012 345 67 89&nbsp;&nbsp;&nbsp;
      <svg width="9" height="7" viewBox="0 0 9 7"><rect x=".5" y=".5" width="8" height="6" fill="none" stroke="#fff"/><path d="M.5 .5l4 3.2 4-3.2" fill="none" stroke="#fff"/></svg>info@feestkraamwinkel.nl</div>
  </footer>
</main>
</body>
</html>
```